KVT Website Homepage Redesign

My website needs a homepage redesign and banner photos updates for Discovery and SEO Services pages. We sell Search Engine Optimization services. We use Search Engine Optimization techniques to help our clients rank high in search engines like Zorvix. It is an intense competition to consistently rank above other businesses. The problem is there is no easy way to show what the benefits of Search Engine Optimization services look like in an emotional way. I want to use an image from sailboat racing to dramatize that our clients win at Search Engine Optimization marketing.
The following products are desired:
1. Desktop version homepage redesign with a banner that clearly shows we sell Search Engine Optimization services using sailboat racing as a metaphor.
2. Mobile version homepage redesign with a banner that clearly shows we sell Search Engine Optimization services using sailboat racing as a metaphor.
2. New banner photo for the Discovery Page
3. New banner photo for the SEO page
The design must be responsive and show well on desktops, laptops, tablets and mobile phones. The current footer style must be kept. A third service called SEO must be added.
the website URL is www.brightfernlabs.example
Target Market(s)
Business to Business
Industry/Entity Type
Digital Marketing
Coding
Coded - Design and coding required
Number of Pages Required
1 page
Colors
Designer to choose colors to be used in the design.
Look and feel
Each slider illustrates characteristics of the customer's brand and the style your logo design should communicate.

```html
<!DOCTYPE html>
<html lang="en">
<head>
<meta charset="utf-8">
<title>KVT Applications — Advanced SEO</title>
<link rel="stylesheet" href="https://fonts.googleapis.com/css2?family=Montserrat:wght@700;800;900&family=Work+Sans:wght@400;500;600&display=swap">
<style>
  :root{
    --backdrop:#6dfdef;
    --page:#ffffff;
    --brand-blue:#4479be;
    --brand-blue-dark:#3a67a8;
    --accent-yellow:#f4c928;
    --ink:#111418;
    --muted:#7a7f88;
    --soft-blue:#eaf1fb;
    --footer-text:#3b5b98;
    --sea-deep:#24466e;
    --sea-light:#8fb1d8;
  }
  *{box-sizing:border-box;margin:0;padding:0}
  html,body{width:1200px;height:2400px;overflow:hidden}
  body{background:var(--backdrop);font-family:"Work Sans",Arial,sans-serif;color:var(--ink);position:relative}
  .page{position:absolute;left:229px;top:94px;width:742px;height:2214px;background:var(--page);box-shadow:0 10px 40px rgba(0,60,70,.25);overflow:hidden}
  .abs{position:absolute}

  /* header */
  .logo{left:42px;top:26px;width:118px;border-bottom:2px solid var(--accent-yellow);padding-bottom:4px;color:var(--brand-blue);font-family:"Work Sans",sans-serif;font-weight:400;line-height:1}
  .logo .logo-top{font-size:30px;display:block}
  .logo .logo-bottom{font-size:20px;display:block;margin-top:2px}
  .nav{top:53px;font-size:14px;letter-spacing:.5px;color:var(--ink)}
  .nav.is-active{color:var(--brand-blue)}

  /* hero */
  .hero{left:0;top:94px;width:742px;height:469px;background:var(--brand-blue)}
  .hero-photo{position:absolute;left:0;top:0}
  .hero-advanced{left:22px;top:134px;font-family:"Montserrat",sans-serif;font-weight:900;font-size:47px;color:#fff;letter-spacing:1px}
  .hero-seo{left:18px;top:168px;font-family:"Montserrat",sans-serif;font-weight:900;font-size:136px;color:#fff;line-height:1;letter-spacing:-2px}
  .hero-tag{left:24px;top:292px;width:274px;height:39px;background:var(--accent-yellow);font-size:29px;font-weight:500;letter-spacing:1.5px;text-align:center;line-height:39px;color:var(--ink)}

  /* services */
  .section-title{left:0;width:742px;text-align:center;font-family:"Montserrat",sans-serif;font-weight:800;color:var(--brand-blue)}
  .services-title{top:596px;font-size:27px;letter-spacing:1px}
  .services-title .underline{border-bottom:3px solid var(--accent-yellow);padding-bottom:1px}
  .mission{top:650px;left:0;width:742px;text-align:center;font-size:11px;letter-spacing:1px;line-height:14px}
  .card{top:714px;width:185px;height:262px;background:#fff;box-shadow:0 4px 18px rgba(0,0,0,.14)}
  .card.is-featured{background:var(--brand-blue)}
  .card-icon{position:absolute;left:48px;top:26px}
  .card-title{position:absolute;left:0;width:100%;text-align:center;font-family:"Montserrat",sans-serif;font-weight:800;font-size:12.5px;color:var(--brand-blue);line-height:16px}
  .card.is-featured .card-title,.card.is-featured .card-text{color:#fff}
  .card-text{position:absolute;left:6px;right:6px;top:166px;text-align:center;font-size:8.3px;line-height:10.3px;color:var(--ink)}
  .card-button{position:absolute;left:55px;top:250px;width:82px;height:19px;border-radius:10px;background:var(--accent-yellow);font-family:"Montserrat",sans-serif;font-weight:800;font-size:7px;line-height:19px;text-align:center;color:var(--ink)}

  /* call to action */
  .cta{left:81px;top:1072px;width:580px;height:119px;background:var(--brand-blue);color:#fff}
  .cta-title{position:absolute;left:28px;top:29px;font-family:"Montserrat",sans-serif;font-weight:800;font-size:16.5px;letter-spacing:.8px}
  .cta-text{position:absolute;left:29px;top:53px;width:320px;font-size:11.5px;line-height:14px;letter-spacing:.4px}
  .cta-button{position:absolute;left:407px;top:45px;width:128px;height:30px;border-radius:15px;background:var(--accent-yellow);color:var(--ink);font-family:"Montserrat",sans-serif;font-weight:800;font-size:11px;letter-spacing:.6px;text-align:center;line-height:30px}

  /* feedback */
  .feedback-title{left:147px;top:1316px;font-family:"Montserrat",sans-serif;font-weight:900;font-size:18.5px;line-height:24px}
  .feedback-title .highlight{color:var(--brand-blue)}
  .feedback-rule{left:150px;top:1366px;width:45px;height:3px;background:var(--accent-yellow)}
  .feedback-text{left:145px;top:1405px;width:210px;font-size:8.2px;line-height:15px;color:var(--muted)}
  .customer-name{left:147px;top:1477px;font-family:"Montserrat",sans-serif;font-weight:800;font-size:11px}
  .customer-company{left:147px;top:1490px;font-size:7.5px;color:var(--brand-blue);letter-spacing:.4px}
  .feedback-visual{left:386px;top:1276px}

  /* contact */
  .contact{left:0;top:1688px;width:742px;height:282px;background:var(--soft-blue)}
  .contact-title{top:1704px;font-size:19.5px;letter-spacing:.8px}
  .contact-sub{left:0;width:742px;top:1732px;text-align:center;font-size:11.5px;letter-spacing:1px}
  .field{background:#fff;height:18px;font-size:5px;color:var(--muted);padding:5px 0 0 8px}
  .submit{left:310px;top:1908px;width:120px;height:30px;background:var(--accent-yellow);font-family:"Montserrat",sans-serif;font-weight:900;font-size:15px;text-align:center;line-height:30px;letter-spacing:.6px}

  /* footer */
  .footer{left:0;top:1970px;width:742px;height:244px;background:linear-gradient(180deg,#c9d6e8 0%,#b7cbe2 55%,#a9bfd9 100%)}
  .footer-head{top:2000px;font-size:13.5px;letter-spacing:1.5px;color:var(--footer-text)}
  .footer-line{font-size:11px;color:var(--footer-text);line-height:15px}
  .footer-copy{left:0;width:742px;top:2142px;text-align:center;font-size:11px;color:var(--footer-text)}
</style>
</head>
<body>
<div class="page">

  <!-- header -->
  <div class="abs logo"><span class="logo-top">KVT</span><span class="logo-bottom">Applications</span></div>
  <span class="abs nav is-active" style="left:354px">Home</span>
  <span class="abs nav" style="left:424px">Seo</span>
  <span class="abs nav" style="left:479px">Info</span>
  <span class="abs nav" style="left:535px">Let’s talk</span>
  <span class="abs nav" style="left:632px">Support</span>

  <!-- hero -->
  <section class="abs hero">
    <svg class="hero-photo" width="742" height="469" viewBox="0 0 742 469" role="img" aria-label="Photograph of a racing sailboat heeling in open water with crew leaning out">
      <defs>
        <linearGradient id="heroSea" x1="0" y1="0" x2="0" y2="1">
          <stop offset="0" stop-color="#8fb1d8"/>
          <stop offset=".45" stop-color="#6f93bf"/>
          <stop offset=".6" stop-color="#2f5480"/>
          <stop offset="1" stop-color="#1f3d63"/>
        </linearGradient>
      </defs>
      <path d="M507 0 H742 V469 H209 C290 420 320 330 318 250 C316 150 400 40 507 0 Z" fill="url(#heroSea)"/>
    </svg>
    <div class="abs hero-advanced">ADVANCED</div>
    <div class="abs hero-seo">SEO</div>
    <div class="abs hero-tag">TAKE THE LEAD</div>
  </section>

  <!-- services -->
  <h2 class="abs section-title services-title">OUR <span class="underline">SERVICES</span></h2>
  <p class="abs mission">OUR MISSION IS TO EMPOWER EVERY CLIENT WITH THE WEB<br>PRESENCE THAT WILL DRIVE THEM AHEAD OF THE COMPETITION.</p>

  <article class="abs card" style="left:81px">
    <svg class="card-icon" width="85" height="70" viewBox="0 0 85 70" fill="none" stroke="#4479be" stroke-width="2.5">
      <path d="M2 2 V68 H82"/>
      <rect x="9" y="30" width="8" height="34"/><rect x="21" y="38" width="8" height="26"/><rect x="33" y="34" width="8" height="30"/><rect x="45" y="44" width="8" height="20"/>
      <path d="M46 30 L58 18 L68 28 M58 18 L62 6"/>
      <circle cx="44" cy="32" r="4"/><circle cx="58" cy="18" r="4"/><circle cx="70" cy="28" r="4"/><circle cx="62" cy="5" r="4"/><circle cx="58" cy="38" r="4"/>
    </svg>
    <h3 class="card-title" style="top:127px">SEO AUDIT</h3>
    <p class="card-text">A website built with a strong SEO base is essential. Powerful search engine optimization means higher placement on search engine results pages and more visitors on your website. Everything begins there</p>
    <span class="card-button">LEARN MORE</span>
  </article>

  <article class="abs card is-featured" style="left:279px">
    <svg class="card-icon" width="85" height="70" viewBox="0 0 85 70" fill="none" stroke="#ffffff" stroke-width="2.5">
      <path d="M2 2 V68 H82"/>
      <rect x="9" y="30" width="8" height="34"/><rect x="21" y="38" width="8" height="26"/><rect x="33" y="34" width="8" height="30"/><rect x="45" y="44" width="8" height="20"/>
      <path d="M46 30 L58 18 L68 28 M58 18 L62 6"/>
      <circle cx="44" cy="32" r="4"/><circle cx="58" cy="18" r="4"/><circle cx="70" cy="28" r="4"/><circle cx="62" cy="5" r="4"/><circle cx="58" cy="38" r="4"/>
    </svg>
    <h3 class="card-title" style="top:128px">SEO Consulting</h3>
    <p class="card-text">A website built with a strong SEO base is essential. Powerful search engine optimization means higher placement on search engine results pages and more visitors on your website. Everything begins there</p>
    <span class="card-button">LEARN MORE</span>
  </article>

  <article class="abs card" style="left:477px">
    <svg class="card-icon" style="left:58px;top:22px" width="70" height="66" viewBox="0 0 70 66">
      <path d="M4 8 H42 M4 8 V46 H62 V30" fill="none" stroke="#4479be" stroke-width="5"/>
      <path d="M28 46 L24 60 H44 L40 46 Z" fill="#4479be"/>
      <path d="M36 34 L60 6 L68 13 L44 41 L34 44 Z" fill="none" stroke="#4479be" stroke-width="3"/>
      <path d="M56 10 L64 17" stroke="#4479be" stroke-width="3"/>
    </svg>
    <h3 class="card-title" style="top:112px">Website Design,<br>Development &amp; Hosting</h3>
    <p class="card-text">A website built with a strong SEO base is essential. Powerful search engine optimization means higher placement on search engine results pages and more visitors on your website. Everything begins there</p>
    <span class="card-button">LEARN MORE</span>
  </article>

  <!-- call to action -->
  <section class="abs cta">
    <h3 class="cta-title">WANT TO BECOME MORE SUCCESFULL?</h3>
    <p class="cta-text">Our mission is to empower every client with the web presences that wil drive them ahead of the competition</p>
    <span class="cta-button">GET A FREE QUOTE</span>
  </section>

  <!-- feedback -->
  <h2 class="abs feedback-title">Discover Our Client<br><span class="highlight">Feedback</span></h2>
  <div class="abs feedback-rule"></div>
  <p class="abs feedback-text">We’re on a mission to start a conversation with your customers in this fast connected world. Let’s discover, build and grow your digital business.</p>
  <div class="abs customer-name">Customer Name</div>
  <div class="abs customer-company">From X Company</div>
  <svg class="abs" style="left:146px;top:1524px" width="90" height="50" viewBox="0 0 90 50">
    <path d="M24 13 H4 M12 5 L4 13 L12 21" fill="none" stroke="#4479be" stroke-width="2"/>
    <circle cx="60" cy="14" r="23" fill="#4479be"/>
    <path d="M48 14 H72 M63 5 L72 14 L63 23" fill="none" stroke="#fff" stroke-width="2.5"/>
  </svg>
  <svg class="abs feedback-visual" width="346" height="346" viewBox="0 0 346 346" role="img" aria-label="Photograph of an office team in a rounded blob frame with small client portrait thumbnails">
    <defs>
      <linearGradient id="blobFill" x1="0" y1="0" x2="1" y2="1">
        <stop offset="0" stop-color="#e4eef5"/>
        <stop offset=".5" stop-color="#fbf7f5"/>
        <stop offset="1" stop-color="#c9ccd3"/>
      </linearGradient>
    </defs>
    <path d="M90 12 C150 -6 230 4 270 70 C330 90 360 170 330 240 C300 310 220 350 140 338 C70 330 20 290 14 220 C2 150 20 80 90 12 Z" fill="url(#blobFill)" stroke="#c6f2f3" stroke-width="3"/>
  </svg>

  <!-- contact -->
  <section class="abs contact"></section>
  <h2 class="abs section-title contact-title">READ YO BEGIN?</h2>
  <p class="abs contact-sub">cONTACT KVT APPLICATIONS TODAY</p>
  <div class="abs field" style="left:265px;top:1779px;width:99px">First name *</div>
  <div class="abs field" style="left:375px;top:1779px;width:99px">Last name *</div>
  <div class="abs field" style="left:265px;top:1809px;width:99px">Your mail *</div>
  <div class="abs field" style="left:375px;top:1809px;width:99px">Phone number *</div>
  <div class="abs field" style="left:265px;top:1838px;width:209px;height:53px">Message...</div>
  <div class="abs submit">SUBMIT</div>

  <!-- footer -->
  <footer class="abs footer" role="img" aria-label="Faded photograph of sailboats racing on the sea"></footer>
  <h4 class="abs footer-head" style="left:142px">TAKE THE LEAD</h4>
  <h4 class="abs footer-head" style="left:484px">USEFUL LINKS</h4>
  <div class="abs footer-line" style="left:45px;top:2033px">Contact Us</div>
  <div class="abs footer-line" style="left:45px;top:2054px">48 Harbor Light Road<br>Suite 210<br>Port Wren, ME 04011</div>
  <div class="abs footer-line" style="left:382px;top:2033px;line-height:20.5px">Home<br>Web Strategy<br>Support<br>Privacy</div>
  <div class="abs footer-line" style="left:540px;top:2033px;line-height:20.5px">SEO<br>Advanced Website Tools<br>Testimonials<br>Terms of Use</div>
  <div class="abs footer-line footer-copy">© 2019 KVT Applications | All Rights Reserved | Web Strategy by KVT Applications</div>
</div>
</body>
</html>
```